Bold Vehicle Wrap Design for 2025 Halvorsen Trekmule Cargo Van

We need a full wrap design for our 2025 Halvorsen-Kraft Trekmule 2500 High Roof Cargo Van. This van will be used to represent Brightmark Pro Services, and we want it to stand out with a bold, professional look.

Vehicle Details:
2025 Trekmule 2500
High Roof
144" Wheelbase
Cargo configuration (no windows)

Our current logo is black, white, and gray — but we’re open to more colorful wrap concepts that could even influence a logo recolor.

We want a wrap design that:
Looks bold and professional
Incorporates icons for the services we provide:Plumbing,Handyman, Land Management, Junk and Debris Removal
Incorporates or complements our current logo
Avoids placing critical text or graphics across sliding doors, seams, or complex panel curves
Download all project files (template, logo, reference images):
https://files.quillbarn-share.com/f/7kq2vz9xw4nm18pd5r/BXTLUmQeKsPOtvc3h8rjnZW?key=2pxd9mwq47vbt6c5ls0eyhz3f&s=k8m3vqrt&dl=0

Target Market(s)

ocal residential and commercial customers in need of professional plumbing, handyman, land management, and junk/debris removal services. Homeowners and property managers looking for reliable and skilled service providers. Businesses and contractors who require prompt, professional, and trustworthy support for their facilities and properties. Customers who value quality workmanship and clear branding that conveys professionalism and expertise.

Industry/Entity Type

Local Service Providers specializing in residential and commercial property maintenance

Requirements
Must have
• Incorporate the Brightmark Pro Services logo with flexibility for adding color to complement the wrap. Use bold, professional, and eye-catching colors that stand out on the road. Include icons or visuals representing these key services: Plumbing Handyman Land Management Junk and Debris Removal. Design must fit a 2025 Halvorsen Trekmule 2500 High Roof Cargo Van (144" WB, cargo version with sliding door) — avoid placing important graphics or text over the sliding door seams or complex curves. Use high-contrast text and graphics for maximum readability from a distance. Design should be modern and clean, but bold enough to be memorable. Wrap design must work on all visible sides: driver side, passenger side, rear, and front. Provide final deliverables in Adobe Illustrator (.ai) or Photoshop (.psd) with layered files.
Nice to have
• Mockup images showing the wrap applied to the van template.
Should not have
• Do not place important text, logos, or graphics across the sliding door seam or uneven panel curves — they may get distorted or hidden.No low-contrast text or graphics that make information hard to read from a distance.Do not include any unrelated images or icons that don’t represent Brightmark Pro Services’ core offerings.Do not create a design that looks too similar to competitors or other well-known brands. No fonts that are hard to read or too decorative for a work vehicle.

```html
<!DOCTYPE html>
<html lang="en">
<head>
<meta charset="utf-8">
<title>Brightmark Pro Services – Van Wrap Side Panel</title>
<link rel="stylesheet" href="https://fonts.googleapis.com/css2?family=Montserrat:wght@500;600;800&display=swap">
<style>
  :root {
    --navy: #193f6f;
    --orange: #de4427;
    --white: #ffffff;
    --page: #ffffff;
  }
  html, body {
    margin: 0;
    padding: 0;
    width: 1200px;
    height: 1199px;
    overflow: hidden;
    background: var(--page);
  }
  .canvas {
    position: relative;
    width: 1200px;
    height: 1199px;
  }
  .wrap-panel {
    position: absolute;
    left: 40px;
    top: 356px;
    width: 1120px;
    height: 486px;
    display: block;
  }
  .panel-base { fill: var(--navy); }
  .band { fill: var(--orange); }
  .pinstripe { fill: none; stroke: var(--white); stroke-width: 5; }
  .headline {
    font-family: "Montserrat", sans-serif;
    font-weight: 600;
    font-size: 56px;
    fill: var(--white);
  }
  .brand-name {
    font-family: "Montserrat", sans-serif;
    font-weight: 800;
    fill: var(--white);
  }
  .contact {
    font-family: "Montserrat", sans-serif;
    font-weight: 600;
    fill: var(--white);
  }
  .contact-icon { fill: none; stroke: var(--white); stroke-width: 2; }
  .chip-box { fill: var(--orange); stroke: #f05a3c; stroke-width: 2; }
  .chip-icon-box { fill: var(--navy); }
  .chip-icon { fill: none; stroke: var(--white); stroke-width: 3; stroke-linecap: round; stroke-linejoin: round; }
  .chip-label {
    font-family: "Montserrat", sans-serif;
    font-weight: 500;
    font-size: 25px;
    fill: var(--white);
  }
</style>
</head>
<body>
<main class="canvas">
  <svg class="wrap-panel" viewBox="0 0 1535 666" role="img" aria-label="Brightmark Pro Services van side wrap layout">
    <rect class="panel-base" x="0" y="0" width="1535" height="666"/>

    <!-- top band -->
    <path class="band" d="M0 0 H1155 L925 120 Q902 134 868 134 H0 Z"/>
    <text class="headline" x="168" y="112">Brightmark Pro Services</text>

    <!-- brand name -->
    <g class="brand-lockup">
      <text class="brand-name" x="205" y="245" font-size="78">BRIGHTMARK</text>
      <text class="brand-name" x="205" y="300" font-size="38" letter-spacing="5">PRO SERVICES</text>
    </g>

    <!-- contact band and swoosh -->
    <path class="band" d="M0 357 H930 C990 357 1025 378 1065 425 L1270 666 H1172 L985 455 C952 423 920 415 862 415 H0 Z"/>
    <path class="pinstripe" d="M0 423 H862 C918 423 945 432 976 464 L1162 666"/>

    <g class="contact-phone">
      <circle class="contact-icon" cx="88" cy="388" r="17"/>
      <path class="contact-icon" d="M80 379 q-3 6 3 14 q6 8 13 6 l2 -4 -5 -3 -3 2 q-4 -3 -6 -7 l2 -3 -3 -5 z"/>
      <text class="contact" x="113" y="402" font-size="38">123-456-7890</text>
    </g>
    <g class="contact-web">
      <circle class="contact-icon" cx="435" cy="388" r="16"/>
      <ellipse class="contact-icon" cx="435" cy="388" rx="7" ry="16"/>
      <path class="contact-icon" d="M419 388 H451 M422 380 H448 M422 396 H448"/>
      <text class="contact" x="464" y="398" font-size="31">www.brightmarkpro.com</text>
    </g>

    <!-- service chips -->
    <g class="chip chip-plumbing">
      <rect class="chip-box" x="64" y="436" width="194" height="39" rx="4"/>
      <rect class="chip-icon-box" x="68" y="440" width="42" height="31" rx="3"/>
      <path class="chip-icon" d="M76 450 V464 M76 455 H98 V464 M86 450 V455 M82 449 H90"/>
      <text class="chip-label" x="118" y="464">Plumbing</text>
    </g>
    <g class="chip chip-handyman">
      <rect class="chip-box" x="268" y="436" width="212" height="39" rx="4"/>
      <rect class="chip-icon-box" x="272" y="440" width="42" height="31" rx="3"/>
      <path class="chip-icon" d="M283 446 L303 466 M303 446 L283 466 M281 448 l4 -4 M301 444 l4 4"/>
      <text class="chip-label" x="323" y="464">Handyman</text>
    </g>
    <g class="chip chip-land">
      <rect class="chip-box" x="490" y="436" width="323" height="39" rx="4"/>
      <rect class="chip-icon-box" x="494" y="440" width="42" height="31" rx="3"/>
      <path class="chip-icon" d="M502 466 H528 M515 466 V456 M515 456 c-6 -2 -6 -10 0 -12 c6 2 6 10 0 12"/>
      <text class="chip-label" x="545" y="464">Land Management</text>
    </g>
    <g class="chip chip-junk">
      <rect class="chip-box" x="490" y="491" width="379" height="39" rx="4"/>
      <rect class="chip-icon-box" x="494" y="495" width="42" height="31" rx="3"/>
      <path class="chip-icon" d="M505 501 L525 521 M525 501 L505 521 M503 503 l4 -4 M523 499 l4 4"/>
      <text class="chip-label" x="545" y="519">Junk &amp; Debris Removal</text>
    </g>
  </svg>
</main>
</body>
</html>
```